Agricultural Consulting Website

Provide a modern yet business like website for my new Agriculture Consulting Business in Australia called FenTrove. Whilst we are based in Australia we are targetting both domestic and international markets (especially in Asia). We are targetting corporate, small business, government and farmer clients. The design should compliment our logo also sourced through pixel guild. The webiste should be easy for me to keep updated on a regular basis without the need to go back to the designer.

Industry/Entity Type

Business

Requirements
Must have
• clean crisp feel
• be modern yet business like
• be able to be updated by myself easily

```html
<!DOCTYPE html>
<html lang="en">
<head>
<meta charset="utf-8">
<title>FenTrove — Agricultural Consulting</title>
<link rel="stylesheet" href="https://fonts.googleapis.com/css2?family=Ubuntu:wght@300;400;500&family=Arvo:wght@400;700&family=Open+Sans:wght@600&family=Pathway+Gothic+One&display=swap">
<style>
:root{
  --green:#5a9a10;
  --green-bright:#6fae1a;
  --brown:#6b3806;
  --brown-dark:#4a2604;
  --text:#5d6470;
  --heading:#3b3b3b;
  --footer:#30313b;
  --footer-text:#d9d9de;
  --panel:rgba(255,255,255,.35);
}
*{box-sizing:border-box;margin:0;padding:0}
html,body{width:1200px;height:971px;overflow:hidden}
body{font-family:"Ubuntu",sans-serif;color:var(--text);background:#fff;position:relative}
a{text-decoration:none;color:inherit}

.site-header{position:absolute;left:0;top:0;width:1200px;height:71px;background:linear-gradient(#fff,#ececec)}
.brand{position:absolute;left:204px;top:10px;display:flex;align-items:center;gap:10px}
.brand-mark{width:44px;height:44px;background:var(--brown)}
.brand-name{font-family:"Ubuntu",sans-serif;font-size:34px;font-weight:400;color:var(--green)}
.account{position:absolute;left:897px;top:4px;font-size:12px;font-family:"Ubuntu",sans-serif}
.account .login{color:var(--green);padding-right:4px;border-right:1px solid #bbb}
.account .register{color:var(--brown);padding-left:3px}
.main-nav{position:absolute;right:208px;top:36px;display:flex;font-family:"Pathway Gothic One",sans-serif;font-size:19px}
.main-nav a{color:var(--brown);margin-left:21px;height:35px;line-height:26px;position:relative}
.main-nav a.active{color:var(--green);padding:0 6px;margin-left:0;border-bottom:3px solid var(--green)}

.hero{position:absolute;left:0;top:71px;width:1200px;height:367px;background:linear-gradient(100deg,#cfd6dc 0%,#e8ecee 30%,#f4f5f3 50%,#c9ccd0 75%,#3a3e48 100%)}
.hero-caption{position:absolute;left:0;bottom:0;width:100%;height:54px;background:rgba(20,20,24,.72)}
.hero-caption p{position:absolute;left:203px;top:0;font-family:"Open Sans",sans-serif;font-weight:600;font-size:21px;line-height:27px;color:#fff}
.slider-dots{position:absolute;left:932px;top:25px;display:flex;gap:7px}
.slider-dots span{width:9px;height:9px;background:var(--green);border:1px solid #cde3a8}
.slider-dots span.current{background:var(--brown);border-color:#c79a6a}

.content-band{position:absolute;left:0;top:438px;width:1200px;height:370px;background:linear-gradient(#9ebde6 0%,#c8d7ea 55%,#d7cdb3 100%)}
.content-panel{position:absolute;left:200px;top:0;width:800px;height:370px;background:var(--panel)}

.welcome{position:absolute;left:223px;top:451px;width:505px}
.welcome h1{font-family:"Arvo",serif;font-weight:400;font-size:17px;color:var(--heading)}
.welcome h1 span{font-family:"Ubuntu",sans-serif;font-size:25px;color:var(--green)}
.welcome p{margin-top:8px;font-size:11.5px;font-weight:300;line-height:15.2px;color:var(--text);text-align:justify}
.read-more{font-family:"Arvo",serif;font-size:11.5px;color:var(--green)}
.welcome .read-more{display:block;text-align:right;margin-top:8px;padding-bottom:6px;border-bottom:1px solid rgba(255,255,255,.55)}

.service{position:absolute;width:200px;display:flex;gap:6px}
.service svg{flex:none;margin-top:2px}
.service h2{font-family:"Arvo",serif;font-size:12px;color:var(--brown-dark);margin-bottom:5px}
.service p{font-size:11.5px;font-weight:300;line-height:15.2px}
.s-corporate{left:221px;top:608px}
.s-small{left:496px;top:608px}
.s-government{left:224px;top:709px}
.s-farmers{left:507px;top:709px}

.news-box{position:absolute;left:760px;top:459px;width:216px;height:185px;background:#fff;border-radius:4px;padding:8px 12px 0}
.news-box h2{font-family:"Arvo",serif;font-size:15px;font-weight:400;color:var(--heading);padding-bottom:7px;border-bottom:1px solid #ddd}
.news-item{padding:9px 0 8px;border-bottom:1px solid #ddd}
.news-item:last-of-type{border:0;padding-bottom:3px}
.news-item .title{display:flex;justify-content:space-between;font-family:"Arvo",serif;font-size:10px;font-weight:700;color:#333;gap:6px}
.news-item .date{color:var(--green);font-weight:400}
.news-item p{font-size:11.5px;font-weight:300;line-height:15.2px;margin-top:3px}

.newsletter{position:absolute;left:772px;top:656px;width:200px}
.newsletter h2{font-family:"Arvo",serif;font-size:15px;font-weight:400;color:var(--heading)}
.newsletter p{font-size:11.5px;font-weight:300;line-height:15.2px;margin-top:4px}
.newsletter .field{margin-top:9px;width:184px;height:31px;background:#fff;border:1px solid #ccc;border-radius:2px}
.newsletter .submit{margin-top:8px;width:105px;height:32px;background:linear-gradient(var(--brown),var(--brown-dark));border-radius:3px;color:#fff;font-family:"Arvo",serif;font-size:14px;text-align:center;line-height:32px}

.site-footer{position:absolute;left:0;top:808px;width:1200px;height:163px;background:var(--footer);color:var(--footer-text)}
.footer-title{font-family:"Arvo",serif;font-size:12px;color:var(--green);position:absolute;top:8px}
.quick-links .footer-title{left:214px}
.quick-links ul{position:absolute;left:217px;top:29px;list-style:none;font-size:11px}
.quick-links li{height:17.2px;line-height:17px;padding-left:11px;position:relative}
.quick-links li::before{content:"";position:absolute;left:0;top:6px;width:4px;height:4px;background:#fff}
.contact-info .footer-title{left:438px}
.map{position:absolute;left:438px;top:30px;width:152px;height:112px;background:linear-gradient(135deg,#ece9e2,#dcdad2);border:3px solid #fff}
.contact-list{position:absolute;left:604px;top:30px;font-size:11px;line-height:15px;list-style:none}
.contact-list li{display:flex;gap:12px;margin-bottom:12px;align-items:flex-start}
.contact-list svg{flex:none;margin-top:1px}
.social{position:absolute;left:628px;top:126px;display:flex;gap:8px;font-size:10px}
.social a{background:#4a4b57;padding:3px 5px;border-radius:2px;color:#fff}
.footer-brand{position:absolute;right:212px;top:16px;display:flex;align-items:center;gap:8px}
.footer-brand .mark{width:40px;height:40px;background:#8e8e92}
.footer-brand span{font-size:18px;color:#8e8e92}
.copyright{position:absolute;right:212px;top:122px;text-align:right;font-size:11px;line-height:15px}
</style>
</head>
<body>

<header class="site-header">
  <a class="brand" href="#"><span class="brand-mark"></span><span class="brand-name">FenTrove</span></a>
  <div class="account"><a class="login" href="#">Login</a><a class="register" href="#">Register</a></div>
  <nav class="main-nav">
    <a class="active" href="#">Home</a>
    <a href="#">About Us</a>
    <a href="#">Services</a>
    <a href="#">Resources</a>
    <a href="#">Faq's</a>
    <a href="#">News</a>
    <a href="#">Contact Us</a>
  </nav>
</header>

<section class="hero" role="img" aria-label="Photo of consultants meeting with clients in a bright office">
  <div class="hero-caption">
    <p>Providing Agricultural Consulting And Eco-friendly Services To Help<br>Farmers Increase Yields And Their Bottom Line</p>
    <div class="slider-dots"><span class="current"></span><span></span><span></span><span></span></div>
  </div>
</section>

<section class="content-band" role="img" aria-label="Photo of ripe wheat ears against a blue sky">
  <div class="content-panel"></div>
</section>

<article class="welcome">
  <h1>Welcome to <span>FenTrove</span></h1>
  <p>Lorem ipsum dolor sit amet, consectetuer adipiscing elit, sed diam nonummy nibh euismod tincidunt ut laoreet dolore magna aliquam erat volutpat. Ut wisi enim ad minim veniam, quis nostrud exerci tation ullamcorper suscipit lobortis nisl ut aliquip ex ea commodo consequat. Duis autem vel eum iriure dolor in hendrerit in vulputate velit esse molestie consequat, vel illum dolore eu feugiat nulla facilisis at vero eros et accumsan et iusto odio dignissim.</p>
  <a class="read-more" href="#">Read More</a>
</article>

<div class="service s-corporate">
  <svg width="40" height="34" viewBox="0 0 40 34"><circle cx="14" cy="8" r="6" fill="#5a9a10"/><circle cx="27" cy="9" r="5" fill="#5a9a10"/><path d="M2 34c0-10 5-16 12-16s12 6 12 16z" fill="#5a9a10"/><path d="M20 20c2-2 4-3 7-3 7 0 11 6 11 14H28c0-4-3-9-8-11z" fill="#5a9a10"/></svg>
  <div><h2>Corporate</h2><p>Sed ut perspiciatis unde omnis iste natus error sti lorem voluptatem accus-antium doloremque laudantium</p></div>
</div>
<div class="service s-small">
  <svg width="40" height="34" viewBox="0 0 40 34"><path d="M3 3h34l3 9H0z" fill="#5a9a10"/><rect x="6" y="14" width="28" height="18" fill="none" stroke="#5a9a10" stroke-width="3"/><rect x="3" y="31" width="34" height="3" fill="#5a9a10"/></svg>
  <div><h2>Small Business</h2><p>Sed ut perspiciatis unde omnis iste natus error sti lorem voluptatem accus-antium doloremque udantium</p></div>
</div>
<div class="service s-government">
  <svg width="36" height="32" viewBox="0 0 36 32"><path d="M18 0L35 8H1z" fill="#5a9a10"/><rect x="2" y="9" width="32" height="3" fill="#5a9a10"/><rect x="5" y="13" width="4" height="14" fill="#5a9a10"/><rect x="12" y="13" width="4" height="14" fill="#5a9a10"/><rect x="20" y="13" width="4" height="14" fill="#5a9a10"/><rect x="27" y="13" width="4" height="14" fill="#5a9a10"/><rect x="1" y="28" width="34" height="4" fill="#5a9a10"/></svg>
  <div><h2>Government</h2><p>Sed ut perspiciatis unde omnis iste natus error sti lorem voluptatem cus-antium doloremque laudantium</p></div>
</div>
<div class="service s-farmers">
  <svg width="22" height="34" viewBox="0 0 22 34"><rect x="10" y="6" width="2" height="28" fill="#5a9a10"/><ellipse cx="11" cy="5" rx="3" ry="5" fill="#5a9a10"/><ellipse cx="6" cy="13" rx="3" ry="5" fill="#5a9a10" transform="rotate(-30 6 13)"/><ellipse cx="16" cy="13" rx="3" ry="5" fill="#5a9a10" transform="rotate(30 16 13)"/><ellipse cx="6" cy="22" rx="3" ry="5" fill="#5a9a10" transform="rotate(-30 6 22)"/><ellipse cx="16" cy="22" rx="3" ry="5" fill="#5a9a10" transform="rotate(30 16 22)"/></svg>
  <div><h2>Farmers</h2><p>Sed ut perspiciatis unde omnis iste natus error sti lorem voluptatem ccus-ntium doloremque laudantium</p></div>
</div>

<aside class="news-box">
  <h2>Latest News</h2>
  <div class="news-item">
    <div class="title"><span>Nova funkce</span><span class="date">11.21.2013</span></div>
    <p>Itaque earum rerum hic tenetur a sapi-ente delectus.</p>
  </div>
  <div class="news-item">
    <div class="title"><span>Kvyberu nyni mate ze dvou sablon</span><span class="date">11.21.2013</span></div>
    <p>Itaque earum rerum hic tenetur a sapi-ente delectus, ut aut reiciendis</p>
  </div>
  <a class="read-more" href="#">Read More</a>
</aside>

<aside class="newsletter">
  <h2>Sign Up for E-Newsletter</h2>
  <p>Odebirejte nas newsletter a neunikne vam zadna dulezita novinka</p>
  <div class="field"></div>
  <div class="submit">Submit</div>
</aside>

<footer class="site-footer">
  <div class="quick-links">
    <h3 class="footer-title">Quick Links</h3>
    <ul><li>Home</li><li>About Us</li><li>Service</li><li>Resources</li><li>Faq's</li><li>News</li><li>Contact Us</li></ul>
  </div>
  <div class="contact-info">
    <h3 class="footer-title">Contact Info</h3>
    <div class="map" role="img" aria-label="Street map showing the office location"></div>
    <ul class="contact-list">
      <li><svg width="12" height="14" viewBox="0 0 12 14"><path d="M6 0a5 5 0 0 0-5 5c0 4 5 9 5 9s5-5 5-9a5 5 0 0 0-5-5z" fill="#fff"/><circle cx="6" cy="5" r="2" fill="#30313b"/></svg><span>Lorem ipsum dolor sit amet,<br>consectetuer.</span></li>
      <li><svg width="12" height="14" viewBox="0 0 12 14"><path d="M2 0h3l1 4-2 1c1 2 2 4 4 5l1-2 3 1v3c0 1-1 2-2 2C5 14 0 9 0 3 0 1 1 0 2 0z" fill="#fff"/></svg><span>0 123 456 789</span></li>
      <li><svg width="14" height="12" viewBox="0 0 14 12"><rect x="0.5" y="1.5" width="13" height="9" fill="none" stroke="#fff"/><path d="M1 2l6 5 6-5" fill="none" stroke="#fff"/></svg><span>info@fentrove.com</span></li>
    </ul>
    <div class="social"><a href="#">Chatter</a><a href="#">Flock</a><a href="#">Linkwell</a></div>
  </div>
  <div class="footer-brand"><span class="mark"></span><span>FenTrove</span></div>
  <p class="copyright">© 2013 FenTrove.<br>All rights reserved Privacy Policy</p>
</footer>

</body>
</html>
```